Recently launched Investment banking and Corporate Advisory firm focused and experienced on Selling

We are looking for a dynamic Brochure that can highlight our areas of focus, experience and expertise.
We have a small but seasoned team of professionals in the organisation and want to showcase our ability to provide Growth and / or exit solutions for our clients.
We are a boutique firm and want to focus on showcasing the fact that we strive for excellence and quality and not quantity.

Our core business avtivity at this time is Sell Side M&A services (this means that we sell private businesses). We are unique in our approach to "partnering businesses" with other companies...not just selling them. We focus more on the "strategic fit" of the potential partner rather than the simple valuation that a potential partner (buyer) would place on the company.

We have really been focusing on "GROWTH and EXIT" strategies for private business owners. Customers usually talk to us for 1 of two main reasons. Their businesses are usually very stable or rapidly growing , often to a point where the owners are no longer comfortable running them on their own. They often need capital for expansion or a team to help them expand their business into other countries and markets. for this we look for a solution for them and often it is finding them a strategic partner who will want to buy the majority of the business. There are also the clients that are looking for an exit strategy (typically they are older and getting ready to retire) they are typically seeking for a way to exit the business (sell the business).

A tagline I often use is "Customer Vision" - We see our customers business and needs through their eyes.

Our company website is www.keldmoorpartners.com and is a work in progress

Target Market(s)

Business Owners (CEO / Presidents)
Mostly Male
Late 40's to late 60's
Very often they will be Engineers
Very Successful and hard working
Many of them looking for GROWTH solutions
Many of them looking for Retirement
We heavily focus on Oil and Gas Service companies, Oil and Gas manufacturing / oilfield services / Technology Companies and Industrial Companies

Industry/Entity Type

Boutique

Font styles to use
Sans Serif

Colors
f37022
33a6d7

Requirements
Must have
• This must be extremely high quality. The people that will receive these brochures are Presidents and CEO's of companies. Every document we give the customer directly reflects the quality of service we will provide for them.
Nice to have
• Pictures tell a great story and can also tell about the areas of experience and expertise that we have

Ideally we'd be interested in a square shaped marketing document (signifies strength and solidness in the business/opportunity) - either 5x5 or 7x7 size in a 4-6 page (double-sided) saddle-stitched booklet.
We'd like to relay an emotion while also describing our business.

```html
<!DOCTYPE html>
<html lang="en">
<head>
<meta charset="utf-8">
<title>Keldmoor Partners Ltd — Customer Vision</title>
<link rel="stylesheet" href="https://fonts.googleapis.com/css2?family=Montserrat:ital,wght@0,200;0,300;0,400;0,800;1,400&display=swap">
<style>
  :root {
    --orange: #f37022;
    --blue: #33a6d7;
    --blue-deep: #1f62ad;
    --blue-pale: #7fc6e8;
    --white: #ffffff;
    --footer-ink: #7a3412;
    --photo-a: #9aa7ad;
    --photo-b: #4f5b63;
  }
  * { margin: 0; padding: 0; box-sizing: border-box; }
  html, body { width: 849px; height: 1200px; overflow: hidden; background: var(--white); }
  body { font-family: "Montserrat", sans-serif; }
  .page { position: relative; width: 849px; height: 1200px; overflow: hidden; }
  .page-shapes { position: absolute; inset: 0; }

  .brand { position: absolute; left: 28px; top: 22px; display: flex; align-items: center; gap: 22px; }
  .brand-dot { width: 78px; height: 78px; border-radius: 50%; background: var(--blue); flex: none; }
  .brand-name { display: flex; flex-direction: column; font-weight: 300; color: var(--blue-deep); line-height: 1; }
  .brand-name-main { font-size: 50px; letter-spacing: 0.5px; }
  .brand-name-sub { font-size: 17px; letter-spacing: 2.4px; text-transform: uppercase; margin-top: 4px; padding-left: 3px; }

  .tagline { position: absolute; right: 44px; top: 640px; text-align: right; color: var(--white); }
  .tagline-title { font-style: italic; font-weight: 400; font-size: 42px; line-height: 1.1; }
  .tagline-sub { font-style: italic; font-weight: 400; font-size: 21px; line-height: 1.3; margin-top: 8px; }

  .headline { position: absolute; left: 0; right: 0; top: 792px; color: var(--white); text-align: center; font-weight: 400; }
  .headline-line { display: block; line-height: 1; white-space: nowrap; position: relative; }
  .thin { font-weight: 200; }
  .bold { font-weight: 800; }
  .line-1 { font-size: 46px; }
  .line-2 { font-size: 44px; margin-top: 2px; left: -12px; }
  .line-3 { font-size: 53px; margin-top: -4px; left: -119px; }
  .line-4 { font-size: 44px; margin-top: -8px; left: 62px; }
  .line-5 { font-size: 48px; margin-top: -4px; left: -36px; }
  .line-6 { font-size: 48px; margin-top: -6px; left: -8px; }

  .site-link { position: absolute; left: 0; right: 0; top: 1137px; text-align: center; font-size: 17px; color: var(--footer-ink); }
</style>
</head>
<body>
<main class="page">
  <svg class="page-shapes" width="849" height="1200" viewBox="0 0 849 1200">
    <defs>
      <linearGradient id="photoTone" x1="0" y1="0" x2="1" y2="1">
        <stop offset="0" stop-color="#9aa7ad"/>
        <stop offset="0.55" stop-color="#7d8a90"/>
        <stop offset="1" stop-color="#4f5b63"/>
      </linearGradient>
      <radialGradient id="mapTone" cx="0.5" cy="0.5" r="0.6">
        <stop offset="0" stop-color="#7fc6e8" stop-opacity="0.28"/>
        <stop offset="1" stop-color="#7fc6e8" stop-opacity="0"/>
      </radialGradient>
    </defs>
    <rect class="base" width="849" height="1200" fill="#ffffff"/>
    <polygon class="hero-photo" role="img" aria-label="Photograph of business people's hands joining coloured puzzle pieces together"
      points="0,131 491,131 536,43 849,43 849,620 456,620 422,656 0,656" fill="url(#photoTone)"/>
    <polygon class="info-panel" points="0,656 422,656 456,620 849,620 849,1110 0,1110" fill="#33a6d7"/>
    <rect class="world-map" role="img" aria-label="Faint world map silhouette"
      x="30" y="700" width="790" height="390" fill="url(#mapTone)"/>
    <polyline class="header-rule" points="0,135 493,135 538,47 849,47" fill="none" stroke="#f37022" stroke-width="9"/>
    <polyline class="panel-rule" points="0,656 422,656 456,620 849,620" fill="none" stroke="#f37022" stroke-width="11"/>
    <polygon class="footer-band" points="0,1105 342,1105 360,1120 849,1120 849,1181 0,1181" fill="#f37022"/>
    <rect class="footer-strip" x="0" y="1181" width="849" height="19" fill="#33a6d7"/>
  </svg>

  <header class="brand">
    <span class="brand-dot"></span>
    <span class="brand-name">
      <span class="brand-name-main">Keldmoor</span>
      <span class="brand-name-sub">Partners Ltd</span>
    </span>
  </header>

  <section class="tagline">
    <h1 class="tagline-title">Customer Vision</h1>
    <p class="tagline-sub">Mergers &amp; Acquisition In The<br>Oil &amp; Gas Industry</p>
  </section>

  <h2 class="headline">
    <span class="headline-line line-1 thin">We Have Really Been</span>
    <span class="headline-line line-2 bold">Focusing On</span>
    <span class="headline-line line-3 bold">"Growth</span>
    <span class="headline-line line-4"><span class="thin">and</span> <span class="bold">Exit"</span></span>
    <span class="headline-line line-5 thin">Strategies For</span>
    <span class="headline-line line-6"><span class="bold">Private Business</span> <span class="thin">Owners</span></span>
  </h2>

  <footer class="site-link">www.keldmoorpartners.com</footer>
</main>
</body>
</html>
```